Banner Ad Graphic Design

I need a banner ad (1450 x 350 px) that advertises our new app coming on line. The website is www.quillstoneapp.io. This is for baseball/softball, baseball on this one. The logos are on the webpage.

Target Market(s)

Baseball Teams

Industry/Entity Type

Baseball/Sports

```html
<!DOCTYPE html>
<html lang="en">
<head>
<meta charset="utf-8">
<title>Quillstone App Banner</title>
<link rel="stylesheet" href="https://fonts.googleapis.com/css2?family=Montserrat:wght@600;700&display=swap">
<style>
  :root {
    --page-bg: #f1f1f1;
    --banner-bg: #ffffff;
    --orange: #e9731b;
    --ink: #111111;
    --white: #ffffff;
    --phone-frame: #1c1c1e;
    --screen-top: #eef1f5;
    --screen-bottom: #d9e4d6;
  }
  * { box-sizing: border-box; margin: 0; padding: 0; }
  html, body {
    width: 1200px;
    height: 1200px;
    overflow: hidden;
    background: var(--page-bg);
    font-family: "Montserrat", sans-serif;
  }
  .banner {
    position: absolute;
    left: 82px;
    top: 475px;
    width: 1035px;
    height: 250px;
    background: var(--banner-bg);
    overflow: hidden;
  }
  .banner-shapes {
    position: absolute;
    inset: 0;
  }
  .brand {
    position: absolute;
    left: 44px;
    top: 100px;
    display: flex;
    align-items: center;
    gap: 10px;
    color: var(--ink);
    font-weight: 700;
    font-size: 26px;
  }
  .brand-mark {
    width: 26px;
    height: 26px;
    background: var(--orange);
    border-radius: 5px;
  }
  .headline {
    position: absolute;
    left: 344px;
    top: 58px;
    width: 360px;
    text-align: center;
    color: var(--ink);
    font-weight: 600;
    font-size: 42px;
    line-height: 44px;
    letter-spacing: 0.5px;
  }
  .download-button {
    position: absolute;
    left: 404px;
    top: 164px;
    width: 204px;
    height: 44px;
    border-radius: 22px;
    background: var(--orange);
    color: var(--white);
    display: flex;
    align-items: center;
    justify-content: center;
    gap: 12px;
    font-weight: 600;
    font-size: 21px;
    letter-spacing: 0.5px;
    box-shadow: 0 3px 5px rgba(0,0,0,0.15);
  }
  .download-icon { width: 26px; height: 26px; }
  .phone {
    position: absolute;
    top: 40px;
    width: 98px;
    height: 182px;
    border-radius: 14px;
    background: var(--phone-frame);
    padding: 4px;
  }
  .phone-left { left: 775px; }
  .phone-right { left: 881px; }
  .phone-screen {
    width: 100%;
    height: 100%;
    border-radius: 11px;
    background: linear-gradient(180deg, var(--screen-top) 0%, var(--screen-top) 45%, var(--screen-bottom) 100%);
  }
</style>
</head>
<body>
  <section class="banner">
    <svg class="banner-shapes" width="1035" height="250" viewBox="0 0 1035 250" aria-hidden="true">
      <path fill="var(--orange)" d="M0,250 C80,120 200,20 330,0 L670,0 C715,40 732,90 722,140 C690,60 600,25 470,25 C300,25 120,120 0,250 Z"/>
      <path fill="var(--orange)" d="M680,250 C760,232 820,205 900,203 C960,201 1000,190 1035,168 L1035,250 Z"/>
    </svg>

    <div class="brand">
      <span class="brand-mark"></span>
      <span class="brand-name">Quillstone</span>
    </div>

    <h1 class="headline">OUR NEW<br>APP COMING</h1>

    <div class="download-button">
      <span>DOWNLOAD</span>
      <svg class="download-icon" viewBox="0 0 26 26" aria-hidden="true">
        <circle cx="13" cy="13" r="11.5" fill="none" stroke="var(--white)" stroke-width="1.8"/>
        <path d="M13 7 V18 M8.5 13.5 L13 18 L17.5 13.5" fill="none" stroke="var(--white)" stroke-width="1.8" stroke-linecap="round" stroke-linejoin="round"/>
      </svg>
    </div>

    <div class="phone phone-left">
      <div class="phone-screen" role="img" aria-label="App screen showing a team roster with player statistics"></div>
    </div>
    <div class="phone phone-right">
      <div class="phone-screen" role="img" aria-label="App screen showing a live game score with a baseball field view"></div>
    </div>
  </section>
</body>
</html>
```